real-estate postcard

I am a real-estate broker and want to send a postcard to expired listings saying something like"Now is the Time to think about a New Beginning with a nice looking house with a sold sign in front

Target Market(s)

people who had their homes on the market and their listing expired

Industry/Entity Type

House

Requirements
Must have
• a nice looking upscale home with a sold sign in front of it; also must have my name and contact information
Marnie Tolvath
Brightfern Realty - Ashmere Office
14 W Parlow Street
Ashmere, IL 60588
312-555-0173
Nice to have
• a saying like " Now is the time to think about new beginnings" maybe with a calendar showing it is already November

```html
<!DOCTYPE html>
<html lang="en">
<head>
<meta charset="utf-8">
<title>New Beginnings Postcard</title>
<link rel="stylesheet" href="https://fonts.googleapis.com/css2?family=Oswald:wght@300;400;600&family=Archivo+Black&family=Roboto+Condensed:wght@700&family=Arimo:wght@400;700&display=swap">
<style>
  :root {
    --brand-red: #d9261c;
    --paper: #ffffff;
    --panel-grey: #e1e1e0;
    --edge-pink: #e9b7bb;
    --ink: #1c1c1c;
    --muted: #8a8a8a;
    --rule: #333333;
  }
  * { box-sizing: border-box; margin: 0; padding: 0; }
  html, body {
    width: 763px; height: 1200px; overflow: hidden;
    background: var(--paper);
  }
  .sheet { position: relative; width: 763px; height: 1200px; }

  .card {
    position: absolute; left: 0; width: 763px;
    border: 1px solid var(--edge-pink);
    background: var(--paper);
  }
  .card--front { top: 0; height: 588px; }
  .card--back  { top: 611px; height: 575px; overflow: hidden; }

  /* Front */
  .headline-panel {
    position: absolute; left: 33px; top: 43px; width: 287px; height: 497px;
    background: var(--brand-red); color: var(--paper);
    text-align: center;
  }
  .flourish-rule {
    position: absolute; left: 50%; transform: translateX(-50%);
    height: 2px; background: var(--paper);
  }
  .headline { position: absolute; top: 72px; left: 0; right: 0; line-height: 1; }
  .headline .light {
    display: block; font-family: "Oswald", sans-serif; font-weight: 300;
    font-size: 35px; letter-spacing: 0.5px;
  }
  .headline .heavy {
    display: block; font-family: "Archivo Black", sans-serif;
    font-size: 32px; letter-spacing: 0.5px;
  }
  .headline .mid {
    display: block; font-family: "Oswald", sans-serif; font-weight: 600;
    font-size: 34px;
  }
  .headline .l1 { margin-bottom: 10px; }
  .headline .l2 { margin-bottom: 8px; }
  .headline .l3 { margin-bottom: 8px; }
  .headline .l4 { margin-bottom: 12px; }
  .headline .l5 { margin-bottom: 10px; }
  .tagline {
    position: absolute; top: 388px; left: 0; right: 0;
    font-family: "Roboto Condensed", sans-serif; font-weight: 700;
    font-size: 20px; line-height: 26px;
  }

  .logo-slot {
    position: absolute; left: 540px; top: 45px; width: 181px; height: 94px;
    border: 1.5px solid var(--ink);
    padding: 16px 0 0 29px;
    font-family: "Roboto Condensed", sans-serif; font-weight: 700;
    font-size: 21px; line-height: 28px; color: var(--muted);
  }

  .calendar-art { position: absolute; left: 345px; top: 272px; width: 370px; height: 240px; }

  /* Back */
  .info-panel {
    position: absolute; left: 0; top: 0; width: 418px; height: 575px;
    background: var(--panel-grey);
  }
  .info-heading {
    position: absolute; left: 51px; top: 68px;
    font-family: "Roboto Condensed", sans-serif; font-weight: 700;
    font-size: 22px; color: var(--brand-red);
  }
  .photo { position: absolute; top: 122px; height: 147px; }
  .photo--home { left: 0; width: 204px; }
  .photo--keys { left: 216px; width: 202px; }
  .services {
    position: absolute; left: 47px; top: 280px; list-style: none;
    font-family: "Arimo", sans-serif; font-weight: 700; font-size: 14.5px;
    line-height: 22px; color: var(--ink);
  }
  .services li::before { content: "\2022\00a0"; }
  .contact-band {
    position: absolute; left: 0; top: 425px; width: 418px; height: 132px;
    background: var(--brand-red); color: var(--paper);
    padding: 10px 0 0 37px;
    font-family: "Arimo", sans-serif; font-weight: 700; font-size: 18.5px; line-height: 23px;
  }

  .stamp-box {
    position: absolute; left: 614px; top: 43px; width: 106px; height: 137px;
    border: 1.5px solid var(--ink);
  }
  .address-line {
    position: absolute; left: 421px; width: 299px; height: 1.5px; background: var(--rule);
  }
</style>
</head>
<body>
<div class="sheet">

  <section class="card card--front">
    <div class="headline-panel">
      <div class="flourish-rule" style="top:58px;width:140px;"></div>
      <h1 class="headline">
        <span class="light l1">NOW IS</span>
        <span class="heavy l2">THE TIME</span>
        <span class="mid l3">TO THINK</span>
        <span class="light l4">ABOUT</span>
        <span class="heavy l5">NEW</span>
        <span class="heavy">BEGINNINGS</span>
      </h1>
      <div class="flourish-rule" style="top:340px;width:230px;height:1.5px;"></div>
      <p class="tagline">“Committed to assisting<br>you with all of your<br>real estate needs!”</p>
    </div>

    <div class="logo-slot">Your company<br>logo here</div>

    <svg class="calendar-art" role="img" aria-label="Desk calendar showing November 2014" viewBox="0 0 370 240">
      <defs>
        <linearGradient id="calendarShade" x1="0" y1="0" x2="0" y2="1">
          <stop offset="0" stop-color="#f4f4f4"/>
          <stop offset="1" stop-color="#dcdcdc"/>
        </linearGradient>
      </defs>
      <polygon points="55,0 300,10 365,215 0,165" fill="url(#calendarShade)"/>
    </svg>
  </section>

  <section class="card card--back">
    <div class="info-panel">
      <h2 class="info-heading">We help you find your dream home</h2>

      <svg class="photo photo--home" role="img" aria-label="Photo of an upscale family home under a blue sky" viewBox="0 0 204 147" preserveAspectRatio="none">
        <defs>
          <linearGradient id="homeTones" x1="0" y1="0" x2="0" y2="1">
            <stop offset="0" stop-color="#3f7fd0"/>
            <stop offset="0.55" stop-color="#b9c3bf"/>
            <stop offset="1" stop-color="#6f8a5a"/>
          </linearGradient>
        </defs>
        <rect width="204" height="147" fill="url(#homeTones)"/>
      </svg>

      <svg class="photo photo--keys" role="img" aria-label="Photo of house keys being handed over in front of a home" viewBox="0 0 202 147" preserveAspectRatio="none">
        <defs>
          <linearGradient id="keysTones" x1="0" y1="0" x2="0" y2="1">
            <stop offset="0" stop-color="#8fb7e0"/>
            <stop offset="0.6" stop-color="#d8d0c4"/>
            <stop offset="1" stop-color="#8aa25e"/>
          </linearGradient>
        </defs>
        <rect width="202" height="147" fill="url(#keysTones)"/>
      </svg>

      <ul class="services">
        <li>Residential, Commercial &amp; Land</li>
        <li>Finding you the right home</li>
        <li>Helping you sell your current home</li>
        <li>Finding investment property</li>
        <li>Assisting with relocation or designing to sell</li>
        <li>Providing information for market analysis</li>
      </ul>

      <address class="contact-band" style="font-style:normal;">
        Marnie Tolvath<br>
        Brightfern Realty - Ashmere Office<br>
        14 W Parlow Street<br>
        Ashmere, IL 60588<br>
        312-555-0173
      </address>
    </div>

    <div class="stamp-box"></div>
    <div class="address-line" style="top:290px;"></div>
    <div class="address-line" style="top:351px;"></div>
    <div class="address-line" style="top:412px;"></div>
  </section>

</div>
</body>
</html>
```